Quiet Harbor Podcast Business Card Design

Needing a business card with the logo design provided for Quiet Harbor Podcast. I am looking for a modern style that fits the current logo.

Info:
Name: Teodor Vask
Title: Creator/Host
Email: teodor@quietharborcast.com
Phone: (555) 274-9163
www.quietharborcast.com
Twitter: @qharborcast
Instagram: @quietharborcastshow
Facebook: Quiet Harbor Podcast

Industry/Entity Type

Business

Font styles to use
Sans Serif

Colors
000000
ffffff

Requirements
Must have
• modern, clean design
Nice to have
• social media contact info

```html
<!DOCTYPE html>
<html lang="en">
<head>
<meta charset="utf-8">
<title>Quiet Harbor Podcast – Business Card</title>
<link href="https://fonts.googleapis.com/css2?family=Mulish:wght@400;600&display=swap" rel="stylesheet">
<style>
  :root {
    --backdrop: #161616;
    --card: #1c1c1c;
    --ink: #ffffff;
    --ink-soft: #d9d9d9;
    --ink-dim: #3a3a3a;
    --mark: #e6e6e6;
  }
  * { box-sizing: border-box; margin: 0; padding: 0; }
  html, body {
    width: 1200px; height: 900px; overflow: hidden;
    background: var(--backdrop);
    font-family: "Mulish", sans-serif;
  }
  .sheet {
    width: 1200px; height: 900px;
    display: flex; flex-direction: column;
    align-items: center; justify-content: center; gap: 40px;
  }
  .card {
    width: 630px; height: 360px;
    background: var(--card);
    position: relative;
    box-shadow: 0 18px 40px rgba(0,0,0,.55);
  }
  /* Front */
  .card--front {
    display: flex; flex-direction: column; align-items: center; justify-content: center;
  }
  .brand-large {
    display: flex; align-items: center; gap: 18px;
    color: var(--mark); font-weight: 600; font-size: 54px; letter-spacing: 1px;
  }
  .brand-large .brand-square {
    width: 34px; height: 34px; background: var(--mark);
  }
  .card--front .site {
    position: absolute; bottom: 40px; left: 0; right: 0; text-align: center;
    color: var(--ink-dim); font-size: 14px; letter-spacing: 2px; font-weight: 600;
  }
  /* Back */
  .card--back {
    display: flex; align-items: center;
    padding: 0 40px;
  }
  .brand-small {
    width: 240px;
    display: flex; flex-direction: column; align-items: center; gap: 14px;
  }
  .brand-small .brand-square {
    width: 56px; height: 56px; background: var(--ink-dim);
  }
  .brand-small .brand-name {
    color: var(--ink-dim); font-weight: 600; font-size: 22px;
    text-transform: uppercase; text-align: center; line-height: 1.25; letter-spacing: 1px;
  }
  .divider {
    width: 2px; height: 220px; background: var(--ink); margin: 0 26px 0 14px;
  }
  .contact { color: var(--ink); }
  .contact .name {
    font-size: 24px; font-weight: 600; letter-spacing: 2px; text-transform: uppercase;
  }
  .contact .role {
    font-size: 16px; letter-spacing: 1px; text-transform: uppercase; color: var(--ink-soft);
    margin-bottom: 14px;
  }
  .contact ul { list-style: none; }
  .contact li {
    display: flex; align-items: center; gap: 12px;
    font-size: 15px; line-height: 23px; letter-spacing: .3px;
  }
  .contact li svg { width: 13px; height: 13px; flex: none; fill: var(--ink); }
  .contact li .dot { width: 11px; height: 11px; background: var(--ink); flex: none; margin: 0 1px; }
  .contact .gap { height: 8px; }
</style>
</head>
<body>
<main class="sheet">
  <section class="card card--front" aria-label="Card front">
    <div class="brand-large"><span class="brand-square"></span>Quiet Harbor</div>
    <p class="site">www.quietharborcast.com</p>
  </section>

  <section class="card card--back" aria-label="Card back">
    <div class="brand-small">
      <span class="brand-square"></span>
      <p class="brand-name">Quiet Harbor Podcast</p>
    </div>
    <div class="divider"></div>
    <div class="contact">
      <p class="name">Teodor Vask</p>
      <p class="role">Creator/Host</p>
      <ul>
        <li><svg viewBox="0 0 16 16"><path d="M3.6 1 6 3.8 4.6 5.6c.9 2 2.7 3.8 4.7 4.7l1.8-1.4L14 11.3 12.8 14C6.8 14 2 9.2 2 3.2z"/></svg>(555) 274-9163</li>
        <li><svg viewBox="0 0 16 16"><path d="M1 3h14v1.2L8 9 1 4.2zM1 6l7 4.8L15 6v7H1z"/></svg>teodor@quietharborcast.com</li>
        <li><svg viewBox="0 0 16 16"><circle cx="8" cy="8" r="6.5" fill="none" stroke="#fff" stroke-width="1.5"/><path d="M1.5 8h13M8 1.5c-3 3.5-3 9.5 0 13M8 1.5c3 3.5 3 9.5 0 13" fill="none" stroke="#fff" stroke-width="1.2"/></svg>www.quietharborcast.com</li>
        <li class="gap"></li>
        <li><span class="dot"></span>Quiet Harbor Podcast</li>
        <li><span class="dot"></span>@qharborcast</li>
        <li><span class="dot"></span>@quietharborcastshow</li>
      </ul>
    </div>
  </section>
</main>
</body>
</html>
```